Beacon Crest Service HVAC Card

Sale, Install, Maintenance Commercial Vent Hood, Ice Machine & Refrigeration
Air Conditioning Heating & Cooling

Industry/Entity Type

Air Conditioning

Contact Information for Business Card

Beacon Crest Service
2847 Marlowe Ave.
San Lino Tx, 79915
Ph. (555) 482-7193 Tomas B. Villareal Owner
Ph. (555) 619-2084 Hugo Saldivar Tec.
E-mail. beaconcrest2847@mailbrook.example

```html
<!DOCTYPE html>
<html lang="en">
<head>
<meta charset="utf-8">
<title>Beacon Crest Service – Business Card</title>
<link rel="stylesheet" href="https://fonts.googleapis.com/css2?family=Great+Vibes&display=swap">
<style>
  :root {
    --card-blue: #2a80ff;
    --edge-navy: #1010c8;
    --title-yellow: #f1ff1c;
    --stripe-orange: #ff8000;
    --ink-white: #ffffff;
  }
  html, body {
    margin: 0;
    padding: 0;
    width: 1200px;
    height: 699px;
    overflow: hidden;
    background: var(--card-blue);
  }
  .card {
    position: relative;
    width: 1200px;
    height: 699px;
    box-sizing: border-box;
    background: var(--card-blue);
    border: 1px solid var(--edge-navy);
    font-family: "Great Vibes", cursive;
    color: var(--ink-white);
  }
  .card__frame {
    position: absolute;
    left: 39px;
    top: 33px;
    width: 1111px;
    height: 638px;
    box-sizing: border-box;
    border: 1px solid var(--edge-navy);
  }
  .card__title-box {
    position: absolute;
    left: 761px;
    top: 48px;
    width: 376px;
    height: 143px;
    box-sizing: border-box;
    padding-top: 22px;
    background: var(--title-yellow);
    display: flex;
    align-items: center;
    justify-content: center;
  }
  .card__title {
    margin: 0;
    font-weight: 400;
    font-size: 42px;
    letter-spacing: 1px;
    color: var(--ink-white);
    white-space: nowrap;
  }
  .card__brand {
    position: absolute;
    left: 480px;
    top: 318px;
    width: 220px;
    text-align: center;
    font-size: 44px;
    line-height: 1.05;
    color: var(--ink-white);
  }
  .contact {
    position: absolute;
    top: 350px;
    width: 340px;
    text-align: center;
    letter-spacing: 3px;
    white-space: nowrap;
  }
  .contact--owner { left: 100px; }
  .contact--tech { left: 711px; }
  .contact__name { font-size: 30px; line-height: 40px; }
  .contact__role { font-size: 28px; line-height: 42px; }
  .contact__phone { font-size: 32px; line-height: 54px; }
  .card__address {
    position: absolute;
    left: 200px;
    top: 518px;
    width: 780px;
    text-align: center;
    font-size: 29px;
    line-height: 38px;
    letter-spacing: 2.5px;
    font-style: normal;
    white-space: nowrap;
  }
  .card__stripe {
    position: absolute;
    left: 39px;
    top: 632px;
    width: 1111px;
    height: 21px;
    background: var(--stripe-orange);
  }
</style>
</head>
<body>
  <main class="card">
    <div class="card__frame"></div>

    <div class="card__title-box">
      <h1 class="card__title">Beacon Crest Service</h1>
    </div>

    <div class="card__brand">Beacon Crest<br>Service</div>

    <section class="contact contact--owner">
      <div class="contact__name">Tomas B. Villareal</div>
      <div class="contact__role">Owner</div>
      <div class="contact__phone">Ph. (555) 482-7193</div>
    </section>

    <section class="contact contact--tech">
      <div class="contact__name">Hugo Saldivar</div>
      <div class="contact__role">Technician</div>
      <div class="contact__phone">Ph. (555) 619-2084</div>
    </section>

    <address class="card__address">
      2847 Marlowe Ave. San Lino Tx, 79915<br>
      E-mail : beaconcrest2847@mailbrook.example
    </address>

    <div class="card__stripe"></div>
  </main>
</body>
</html>
```